Cedar Ridge Lakemont Dining Fortnight

We need our flyer from last year updated. Please use this year's logo, attached below and use a similar overall layout as last year's flyer, which is also attached. The goal is to make this year's flyer less cluttered.

1. Remove the cornucopia/food background, and instead incorporate an attractive table, wine glass(es) and possibly a wine bottle.

2. Include this year's logo, attached, prominently in the middle of the flyer, possibly larger.

3. Take out the prices and the 4 buttons/circles with the price options all together.

4. Include the logos for Lantern Fair and the Cedar Ridge Civic Quarter (with the fountain), attached.

The website should be changed to: CRLDiningFortnight.example

```html
<!DOCTYPE html>
<html lang="en">
<head>
<meta charset="utf-8">
<title>Cedar Ridge Lakemont Dining Fortnight</title>
<link rel="stylesheet" href="https://fonts.googleapis.com/css2?family=Oswald:wght@500&family=Courier+Prime:wght@400;700&display=swap">
<style>
  :root {
    --page: #ffffff;
    --wood-dark: #3e3128;
    --wood-mid: #5e4b3d;
    --wood-light: #7a6656;
    --maroon: #5c1820;
    --cloth-red: #d83530;
    --cloth-light: #e8645f;
    --ink-white: #ffffff;
    --ink-dark: #3a1a1e;
    --shadow: rgba(0, 0, 0, 0.55);
  }
  * { margin: 0; padding: 0; box-sizing: border-box; }
  html, body { width: 1200px; height: 1200px; overflow: hidden; background: var(--page); }
  .canvas { position: relative; width: 1200px; height: 1200px; }

  .flyer {
    position: absolute; left: 247px; top: 18px; width: 686px; height: 1140px;
    overflow: hidden;
  }
  .wood-backdrop {
    position: absolute; inset: 0;
    background: linear-gradient(90deg, var(--wood-dark), var(--wood-mid) 30%, var(--wood-light) 55%, var(--wood-mid) 80%, var(--wood-dark));
  }
  .tablecloth { position: absolute; left: 0; top: 0; width: 686px; height: 1140px; }

  .event-mark {
    position: absolute; left: 113px; top: 120px; width: 474px;
    text-align: center; color: var(--ink-white);
    font-family: "Courier Prime", monospace; font-weight: 700;
  }
  .event-name { font-size: 44px; line-height: 1.2; }
  .event-date { margin-top: 26px; font-size: 28px; }

  .host {
    position: absolute; left: 0; width: 686px; top: 518px; text-align: center;
    color: var(--ink-white); font-family: "Courier Prime", monospace;
    text-shadow: 0 2px 6px var(--shadow);
  }
  .host-label { font-size: 23px; font-weight: 400; }
  .host-title { font-size: 29px; font-weight: 700; margin-top: 6px; }
  .host-name { font-size: 44px; font-weight: 700; margin-top: 4px; }

  .site-ribbon {
    position: absolute; left: 322px; top: 772px; width: 618px; height: 63px;
    background: var(--maroon);
    clip-path: polygon(0 0, 100% 0, 100% 100%, 0 100%, 22px 50%);
    display: flex; align-items: center; justify-content: center;
    color: var(--ink-white); font-family: "Courier Prime", monospace;
    font-weight: 700; font-size: 27px; letter-spacing: 1px;
  }
  .ribbon-shadow {
    position: absolute; left: 340px; top: 790px; width: 620px; height: 60px;
    background: var(--shadow); filter: blur(10px);
  }

  .social-bar {
    position: absolute; left: 233px; top: 877px; width: 662px; height: 48px;
    background: var(--page);
    clip-path: polygon(0 0, 96% 0, 100% 100%, 0 100%);
    display: flex; align-items: center; gap: 30px; padding-left: 40px;
    font-family: "Courier Prime", monospace; font-size: 11px; color: var(--ink-dark);
  }
  .social-item { display: flex; align-items: center; gap: 6px; }
  .social-mark { width: 15px; height: 15px; background: var(--ink-dark); }

  .partner-shadow {
    position: absolute; left: 712px; top: 982px; width: 245px; height: 150px;
    background: var(--shadow); filter: blur(12px);
  }
  .partner-panel {
    position: absolute; left: 695px; top: 965px; width: 245px; height: 153px;
    background: var(--page);
    display: flex; align-items: center; justify-content: center; gap: 14px;
    font-family: "Oswald", sans-serif; font-weight: 500; font-size: 16px;
    color: var(--maroon); text-transform: uppercase; text-align: center; line-height: 1.15;
  }
  .partner { display: flex; flex-direction: column; align-items: center; gap: 6px; width: 90px; }
  .partner-dot { width: 16px; height: 16px; border-radius: 50%; background: var(--maroon); }
  .partner-divider { width: 1px; height: 110px; background: var(--ink-dark); }
</style>
</head>
<body>
<main class="canvas">
  <section class="flyer">
    <div class="wood-backdrop" role="img" aria-label="Weathered dark wooden plank tabletop"></div>
    <svg class="tablecloth" viewBox="0 0 686 1140" role="img" aria-label="Red and white checked tablecloth draped diagonally across the table">
      <polygon points="0,1040 598,637 686,715 686,1140 0,1140" fill="var(--cloth-red)"/>
      <polygon points="420,1140 560,1000 686,1000 686,1140" fill="var(--cloth-light)" opacity="0.35"/>
    </svg>

    <div class="event-mark">
      <p class="event-name">Cedar Ridge<br>Lakemont<br>Dining Fortnight</p>
      <p class="event-date">September 6 – 11, 2016</p>
    </div>

    <div class="host">
      <p class="host-label">Hosted by:</p>
      <p class="host-title">Harlow County Councilmember</p>
      <p class="host-name">Dana Whitfield</p>
    </div>
  </section>

  <div class="ribbon-shadow"></div>
  <div class="site-ribbon">www.CRLDiningFortnight.example</div>

  <div class="social-bar">
    <span class="social-item"><span class="social-mark"></span>Cedarridgediningfortnight</span>
    <span class="social-item"><span class="social-mark"></span>@CedarRidgeDF #CRDF</span>
    <span class="social-item"><span class="social-mark"></span>@cedarridgediningfortnight</span>
  </div>

  <div class="partner-shadow"></div>
  <div class="partner-panel">
    <div class="partner"><span class="partner-dot"></span>Cedar Ridge Civic Quarter</div>
    <div class="partner-divider"></div>
    <div class="partner"><span class="partner-dot"></span>Lantern Fair</div>
  </div>
</main>
</body>
</html>
```